TRESSAVO FACEBOOK DESIGN

I need new design for facebook https://www.facebook.com/tressavoclinica.
Our Businnes is Hair care , hair replacement , hair transplant . hair regrowth . i NEED MEDICAL AND PROFESSIONAL DESIGN. I NEED ALSO RESPONSIVE DESIGN

Target Market(s)

Consumers

Industry/Entity Type

MEDICAL AND COSMETICS

Colors
0054AA
0677BA
7BADD7
CADEEF
E8F1F8

Requirements
Must have
• MEDICAL
Nice to have
• RESPONSIVE DESIGN

```html
<!DOCTYPE html>
<html lang="it">
<head>
<meta charset="utf-8">
<title>Tressavo – Facebook Cover</title>
<link rel="stylesheet" href="https://fonts.googleapis.com/css2?family=Poppins:wght@500;600;700&display=swap">
<style>
  :root {
    --brand-deep: #0054aa;
    --brand-navy: #0d4a96;
    --brand-mid: #0677ba;
    --brand-sky: #2aa9e0;
    --brand-soft: #7badd7;
    --brand-pale: #cadeef;
    --brand-mist: #e8f1f8;
    --accent-lime: #b9d66a;
    --page-bg: #dfe8f1;
    --white: #ffffff;
  }
  html, body {
    margin: 0;
    width: 1200px;
    height: 900px;
    overflow: hidden;
    background: var(--page-bg);
  }
  .cover {
    position: absolute;
    left: 40px;
    top: 235px;
    width: 1120px;
    height: 429px;
    display: block;
    background: var(--white);
  }
  .band-deep { fill: var(--brand-navy); }
  .band-stripe { fill: var(--brand-sky); }
  .swoosh { fill: none; stroke: var(--brand-sky); stroke-width: 3; stroke-linecap: round; }
  .brand-dot { fill: var(--brand-sky); }
  .brand-name { font-family: "Poppins", sans-serif; font-weight: 600; font-size: 62px; fill: var(--brand-deep); }
  .tagline { font-family: "Poppins", sans-serif; font-weight: 500; font-size: 17.5px; fill: var(--brand-deep); letter-spacing: 0.3px; }
  .services { font-family: "Poppins", sans-serif; font-weight: 700; font-size: 14.5px; fill: var(--brand-deep); }
  .phone-pill { fill: var(--brand-sky); }
  .phone-number { font-family: "Poppins", sans-serif; font-weight: 700; font-size: 27px; fill: var(--white); }
  .ring-outer { fill: none; stroke: var(--brand-sky); stroke-width: 1.5; }
  .ring-arc { fill: none; stroke: var(--brand-sky); stroke-width: 9; }
  .ring-inner { fill: none; stroke: var(--white); stroke-width: 3; }
  .dot-lime { fill: var(--accent-lime); opacity: 0.85; }
  .dot-blue { fill: var(--brand-sky); opacity: 0.55; }
</style>
</head>
<body>
<svg class="cover" viewBox="0 0 888 340" xmlns="http://www.w3.org/2000/svg">
  <defs>
    <linearGradient id="portraitTone" x1="0" y1="0" x2="0" y2="1">
      <stop offset="0" stop-color="#d9a9c4"/>
      <stop offset="0.55" stop-color="#c9b3bf"/>
      <stop offset="1" stop-color="#b9b6b8"/>
    </linearGradient>
  </defs>

  <!-- lower wave bands -->
  <path class="band-deep" d="M0,195 C40,300 200,335 360,322 C470,310 540,278 600,258 L888,205 L888,340 L0,340 Z"/>
  <path class="band-stripe" d="M95,306 C260,312 430,282 610,232 L630,250 C450,300 270,322 95,306 Z"/>

  <!-- brand lockup -->
  <circle class="brand-dot" cx="126" cy="72" r="26"/>
  <text class="brand-name" x="168" y="94">Tressavo</text>
  <text class="tagline" x="256" y="146" text-anchor="middle">CURA E REINTEGRAZIONE DEI CAPELLI</text>
  <path class="swoosh" d="M92,172 Q255,198 418,156"/>

  <!-- services and phone -->
  <text class="services" x="256" y="221" text-anchor="middle">• HAIR CARE • HAIR REPLACEMENT • HAIR TRANSPLANT</text>
  <rect class="phone-pill" x="128" y="238" width="216" height="35" rx="9"/>
  <text class="phone-number" x="236" y="265" text-anchor="middle">321-555-0147</text>

  <!-- portrait frame -->
  <circle class="ring-outer" cx="712" cy="170" r="158"/>
  <path class="ring-arc" d="M712,15 A155,155 0 0 0 612,288"/>
  <circle cx="712" cy="172" r="140" fill="url(#portraitTone)" role="img" aria-label="Photo of a smiling young woman in hair rollers and a bathrobe, surrounded by hair care products"/>
  <circle class="ring-inner" cx="712" cy="172" r="140"/>

  <!-- decorative dots -->
  <circle class="dot-lime" cx="535" cy="110" r="6"/>
  <circle class="dot-lime" cx="558" cy="165" r="14"/>
  <circle class="dot-lime" cx="855" cy="64" r="7"/>
  <circle class="dot-blue" cx="847" cy="102" r="15"/>
  <circle class="dot-blue" cx="860" cy="148" r="24"/>
  <circle class="dot-blue" cx="558" cy="250" r="32"/>
</svg>
</body>
</html>
```